当社 ㈱セキレイワークスの年賀状(デザイン⾯のみ)です。
400枚ほどをクライアント、雑誌社等の媒体、広告代理店、印刷会社など取引先に送ります。
ハガキサイズ(148×100㎜)。特⾊2⾊刷。
デザインは⾃由です。あくまで参考ですが、これまでの年賀状の抜粋を添付します。加えて当社のロゴデータを添付します。
【記載の文面】
明けましておめでとうございます。
私たちはアグレッシブに、元気に、正しきことに労を惜しまず、ブランドに対する思い⼊れとこだわりを⼤切に、本年も更に皆様のお役に⽴てる存在を⽬指します。
株式会社セキレイワークス
代表取締役会⻑ ○○○○ 代表取締役社⻑ ○○○○ 社員⼀同
当社ホームページ
http://www.sekirei-works.example/

当社がファッションに特化した広告会社という事と、2015年干支の羊に掛けて、ウール100%を模した下げ札をあしらった工夫が面白かったです。またデザインもシンプルでかわいらしく思いました。

この度はご提案ありがとうございました。
様々なデザインを面白く拝見させていただきました。
今後も機会ございましたら宜しくお願いいたします。

```html
<!DOCTYPE html>
<html lang="ja">
<head>
<meta charset="utf-8">
<title>年賀状 2015 — セキレイワークス</title>
<link rel="stylesheet" href="https://fonts.googleapis.com/css2?family=Noto+Sans+JP:wght@400;700&family=Noto+Serif:wght@400&display=swap">
<style>
  :root {
    --ink: #111111;
    --red: #c8161d;
    --paper: #ffffff;
    --grey: #444444;
  }
  html, body {
    margin: 0;
    padding: 0;
    width: 808px;
    height: 1200px;
    overflow: hidden;
    background: var(--paper);
  }
  .card {
    position: relative;
    width: 808px;
    height: 1200px;
    background: var(--paper);
    overflow: hidden;
  }
  .frame { position: absolute; }
  .frame--top-left    { left: 0; top: 0; width: 404px; height: 30px; background: var(--ink); }
  .frame--top-right   { left: 404px; top: 0; width: 404px; height: 30px; background: var(--red); }
  .frame--left        { left: 0; top: 0; width: 26px; height: 1200px; background: var(--ink); }
  .frame--right       { right: 0; top: 0; width: 26px; height: 1200px; background: var(--red); }
  .frame--bottom-left { left: 0; bottom: 0; width: 404px; height: 22px; background: var(--ink); }
  .frame--bottom-right{ left: 404px; bottom: 0; width: 404px; height: 22px; background: var(--red); }

  .zodiac {
    position: absolute;
    left: 60px;
    top: 150px;
    width: 600px;
    height: 240px;
  }
  .zodiac__horse {
    position: absolute;
    left: 10px; top: 20px;
    width: 210px; height: 200px;
    background: var(--ink);
    border-radius: 40% 50% 30% 30%;
  }
  .zodiac__arrow {
    position: absolute;
    left: 215px; top: 102px;
    width: 135px; height: 30px;
  }
  .zodiac__sheep {
    position: absolute;
    left: 360px; top: 20px;
    width: 215px; height: 200px;
    background: var(--red);
    border-radius: 45% 45% 30% 30%;
  }

  .greeting {
    position: absolute;
    left: 0; right: 0;
    top: 475px;
    text-align: center;
    font-family: "Noto Serif", serif;
    color: var(--ink);
  }
  .greeting__title {
    margin: 0;
    font-weight: 400;
    font-size: 38px;
    letter-spacing: 2px;
  }
  .greeting__year {
    margin: 4px 0 0;
    font-size: 60px;
    font-weight: 400;
    line-height: 1.1;
  }
  .accent { color: var(--red); }

  .message {
    position: absolute;
    left: 118px;
    top: 845px;
    font-family: "Noto Sans JP", sans-serif;
    font-weight: 700;
    font-size: 18px;
    line-height: 1.72;
    color: var(--ink);
    margin: 0;
  }
  .signatories {
    position: absolute;
    left: 118px;
    top: 1070px;
    font-family: "Noto Sans JP", sans-serif;
    font-size: 13px;
    line-height: 1.75;
    color: var(--grey);
    margin: 0;
  }
  .company {
    position: absolute;
    left: 118px;
    top: 1136px;
    display: flex;
    align-items: center;
    gap: 8px;
    font-family: "Noto Sans JP", sans-serif;
    font-size: 15px;
    font-weight: 400;
    color: var(--ink);
    letter-spacing: 0.5px;
  }
  .company__mark {
    width: 18px; height: 18px;
    border-radius: 50%;
    border: 2px solid var(--ink);
    box-sizing: border-box;
  }
</style>
</head>
<body>
<main class="card">
  <div class="frame frame--top-left"></div>
  <div class="frame frame--top-right"></div>
  <div class="frame frame--left"></div>
  <div class="frame frame--right"></div>
  <div class="frame frame--bottom-left"></div>
  <div class="frame frame--bottom-right"></div>

  <section class="zodiac">
    <div class="zodiac__horse" role="img" aria-label="黒い駆ける馬のシルエット(午年)"></div>
    <svg class="zodiac__arrow" viewBox="0 0 135 30" aria-hidden="true">
      <rect x="0" y="11" width="62" height="8" fill="var(--ink)"/>
      <rect x="62" y="11" width="52" height="8" fill="var(--red)"/>
      <polygon points="108,3 135,15 108,27" fill="var(--red)"/>
    </svg>
    <div class="zodiac__sheep" role="img" aria-label="赤い羊のシルエット(未年)"></div>
  </section>

  <header class="greeting">
    <h1 class="greeting__title">A HAPPY <span class="accent">N</span>EW YEAR</h1>
    <p class="greeting__year">20<span class="accent">15</span></p>
  </header>

  <p class="message">
    明けましておめでとうございます。<br>
    私たちはアグレッシブに、元気に、<br>
    正しきことに労を惜しまず、<br>
    ブランドに対する思い入れとこだわり<span class="accent">を大切に、</span><br>
    本年も更に皆様のお役に立てる存在を<span class="accent">目指します。</span>
  </p>

  <p class="signatories">
    代表取締役会長 ○○○○<br>
    代表取締役社長 ○○○○ 社員一同
  </p>

  <div class="company">
    <span class="company__mark"></span>
    <span class="company__name">SEKIREI WORKS INC.</span>
  </div>
</main>
</body>
</html>
```